Business Card Designs

Looking to design a 3.5" x 2" standard business card for our employees.
The design needs to be sleek, simple, and modern. We would like our logo (attached) to be incorporated, but not in that colour, rather an outline of the logo in either gold or silver (whichever looks better).

Modern and Simple is what we are looking for, but be creative in incorporating the logo.

```html
<!DOCTYPE html>
<html lang="en">
<head>
<meta charset="UTF-8">
<title>Harbourline Residences – Business Card</title>
<link href="https://fonts.googleapis.com/css2?family=Montserrat:wght@400;500;600&display=swap" rel="stylesheet">
<style>
  :root {
    --backdrop: #6f5538;
    --card: #121212;
    --silver: #d6d6d6;
    --white: #ffffff;
    --teal: #5bb5ad;
    --text: #f2f2f2;
  }
  html, body {
    margin: 0;
    padding: 0;
    width: 900px;
    height: 1200px;
    overflow: hidden;
    background: var(--backdrop);
    font-family: "Montserrat", sans-serif;
  }
  .canvas {
    position: relative;
    width: 900px;
    height: 1200px;
  }
  .card {
    position: absolute;
    left: 78px;
    width: 744px;
    height: 442px;
    background: var(--card);
    border-radius: 36px;
    box-shadow: 0 4px 10px rgba(0,0,0,0.45);
  }
  .card--front { top: 130px; }
  .card--back  { top: 638px; }

  .brand {
    position: absolute;
    color: var(--silver);
    font-weight: 600;
    text-align: center;
    text-transform: uppercase;
    line-height: 1.15;
  }
  .card--front .brand {
    left: 100px;
    top: 290px;
    transform: translateY(-130px);
    width: 230px;
    font-size: 22px;
    letter-spacing: 2px;
  }
  .brand__mark {
    display: block;
    width: 18px;
    height: 18px;
    margin: 0 auto 16px;
    background: var(--silver);
  }
  .card--back .brand {
    left: 0;
    right: 0;
    top: 150px;
    font-size: 34px;
    letter-spacing: 3px;
  }
  .card--back .brand__mark {
    width: 26px;
    height: 26px;
    margin-bottom: 22px;
  }

  .divider {
    position: absolute;
    left: 362px;
    top: 137px;
    width: 1.5px;
    height: 196px;
    background: var(--white);
  }
  .details {
    position: absolute;
    left: 413px;
    top: 130px;
    color: var(--text);
  }
  .details__name {
    margin: 0;
    font-size: 27px;
    font-weight: 600;
    color: var(--teal);
    line-height: 1;
  }
  .details__role {
    margin: 4px 0 0;
    font-size: 15px;
    font-weight: 400;
    line-height: 1;
  }
  .details__address {
    margin: 24px 0 0 4px;
    font-style: normal;
    font-size: 16px;
    line-height: 20px;
  }
  .contact {
    list-style: none;
    margin: 28px 0 0 4px;
    padding: 0;
    font-size: 16px;
  }
  .contact li {
    display: flex;
    align-items: center;
    height: 24.5px;
  }
  .contact svg {
    width: 14px;
    height: 14px;
    margin-right: 9px;
    fill: var(--teal);
  }
</style>
</head>
<body>
<main class="canvas">

  <section class="card card--front">
    <div class="brand">
      <span class="brand__mark"></span>
      Harbourline<br>Residences
    </div>
    <div class="divider"></div>
    <div class="details">
      <h1 class="details__name">Daniel Reyes</h1>
      <p class="details__role">owner</p>
      <address class="details__address">
        4420 Cedar Lane, Suite 305<br>
        Westbrook, FL 33190
      </address>
      <ul class="contact">
        <li>
          <svg viewBox="0 0 14 14" aria-hidden="true"><path d="M1 5.5C1 3 4 2 7 2s6 1 6 3.5l-2.5.8-.7-1.8H4.2l-.7 1.8zM3.5 7h7l1.5 5H2z"/></svg>
          (555) 310-4827
        </li>
        <li>
          <svg viewBox="0 0 14 14" aria-hidden="true"><path d="M1 3h12v1.2L7 8 1 4.2zM1 5.6l6 3.8 6-3.8V11H1z"/></svg>
          hello@samplemail.com
        </li>
        <li>
          <svg viewBox="0 0 14 14" aria-hidden="true"><circle cx="7" cy="7" r="6"/></svg>
          www.examplesite.com
        </li>
      </ul>
    </div>
  </section>

  <section class="card card--back">
    <div class="brand">
      <span class="brand__mark"></span>
      Harbourline<br>Residences
    </div>
  </section>

</main>
</body>
</html>
```